Business Card design for new private practice opening

I need a business card design for my new private practice with my new logo uploaded as a file
On the front the logo
On the back: maybe a small logo somewhere?
Priv. Doz. DDr. Corinna Vestaluk
Fachärztin für Allgemein- & Viszeralchirurgie
Address: xxx
Tel: xxx
Mobil:xxx
Webseite:xxx
Email:xxx

Contact Information for Business Card

See project description above for details

Requirements
Nice to have
• I would like the colors of the logo incorporated into the business card

```html
<!DOCTYPE html>
<html lang="de">
<head>
<meta charset="utf-8">
<title>Vestaluk Chirurgie – Visitenkarte</title>
<link rel="stylesheet" href="https://fonts.googleapis.com/css2?family=Montserrat:wght@400;500;600&display=swap">
<style>
  :root {
    --backdrop: #e6e6e6;
    --card: #ffffff;
    --teal: #4fb5b5;
    --logo-grey: #7b7b7b;
    --text-dark: #4a4a4a;
    --text: #555555;
  }
  html, body {
    margin: 0;
    padding: 0;
    width: 1200px;
    height: 513px;
    overflow: hidden;
    background: var(--backdrop);
    font-family: "Montserrat", sans-serif;
  }
  .canvas {
    position: relative;
    width: 1200px;
    height: 513px;
  }
  .card {
    position: absolute;
    top: 89px;
    width: 540px;
    height: 334px;
    background: var(--card);
    overflow: hidden;
  }
  .card--front { left: 30px; }
  .card--back  { left: 638px; }

  .brand-mark {
    position: absolute;
    border-radius: 50%;
    background: var(--teal);
  }
  .brand-name {
    position: absolute;
    margin: 0;
    font-weight: 500;
    color: var(--logo-grey);
    text-transform: uppercase;
    white-space: nowrap;
  }

  /* Front */
  .card--front .brand-mark {
    left: 58px;
    top: 100px;
    width: 134px;
    height: 134px;
  }
  .card--front .brand-name {
    left: 211px;
    top: 112px;
    font-size: 48px;
    line-height: 51px;
    letter-spacing: 0;
  }
  .accent-rule {
    position: absolute;
    left: 0;
    right: 0;
    top: 300px;
    height: 2px;
    background: var(--teal);
  }

  /* Back */
  .card--back .brand-mark {
    left: 29px;
    top: 33px;
    width: 60px;
    height: 60px;
  }
  .card--back .brand-name {
    left: 97px;
    top: 41px;
    font-size: 20px;
    line-height: 24px;
  }
  .contact {
    position: absolute;
    left: 239px;
    top: 107px;
    margin: 0;
    font-size: 17px;
    line-height: 22.4px;
    color: var(--text);
    font-style: normal;
    white-space: nowrap;
  }
  .contact__name {
    font-weight: 600;
    color: var(--text-dark);
  }
  .contact__gap { height: 22.4px; }
</style>
</head>
<body>
<main class="canvas">
  <section class="card card--front" aria-label="Vorderseite">
    <span class="brand-mark" aria-hidden="true"></span>
    <p class="brand-name">Vestaluk<br>Chirurgie</p>
    <span class="accent-rule" aria-hidden="true"></span>
  </section>

  <section class="card card--back" aria-label="Rückseite">
    <span class="brand-mark" aria-hidden="true"></span>
    <p class="brand-name">Vestaluk<br>Chirurgie</p>
    <address class="contact">
      <div class="contact__name">Priv. Doz. DDr. Corinna Vestaluk</div>
      <div>Fachärztin für Allgemein-</div>
      <div>&amp; Viszeralchirurgie</div>
      <div class="contact__gap"></div>
      <div>Address: xxx</div>
      <div>Tel: xxx</div>
      <div>Mobil: xxx</div>
      <div>Webseite: xxx</div>
      <div>Email: xxx</div>
    </address>
  </section>
</main>
</body>
</html>
```